International PR and marketing agency needs website design

We need a branding website, for a company based in the US (Washington DC). We are a communication (PR, marketing, social media) agency. We already have the copy, and we have some example websites (some major agencies), that we like.
For example:
https://pellowtrask.example/
https://durnevaleglobal.example/
https://varnok.example/
https://qmf-reach.example/
https://www.thornbury.example/
The website must be a multi-language site, we will add the new languages step-by-step.
We would like to upload content continuously.
The website has to have sub-pages (segments), and news part.
Target Market(s)
Global
Industry/Entity Type
Public relations, Communications, Marketing, Social Media
Number of Pages Required
5+ page
Font styles to use
Other font styles liked:
- Well readable, modern style.
Look and feel

```html
<!DOCTYPE html>
<html lang="en">
<head>
<meta charset="utf-8">
<title>Nuvara PR — Communication Agency</title>
<link rel="stylesheet" href="https://fonts.googleapis.com/css2?family=Poppins:wght@400;500;600;700&family=Righteous&display=swap">
<style>
:root{
  --pink:#f7d3e6;
  --pink-soft:#fbe9f2;
  --pink-card:#f7d6e7;
  --purple:#951f6f;
  --purple-dark:#7e0f59;
  --red:#d7102f;
  --ink:#2d2d2d;
  --text:#4a4a4a;
  --white:#ffffff;
  --black:#0b0b0b;
}
*{box-sizing:border-box;margin:0;padding:0}
html,body{width:1200px;height:4702px;overflow:hidden}
body{position:relative;background:var(--white);font-family:"Poppins",sans-serif;color:var(--text)}
.abs{position:absolute}
.display{font-family:"Righteous",sans-serif;color:var(--purple);text-transform:uppercase;font-weight:400;letter-spacing:1px}
.section-title{position:absolute;left:0;width:1200px;text-align:center;font-size:34px;line-height:40px}
.smile{display:block;margin:-4px auto 0;width:56px;height:14px}

/* header */
.site-header{position:absolute;top:0;left:0;width:1200px;height:93px;background:var(--pink);z-index:5}
.nav-link{position:absolute;top:38px;font-size:14px;line-height:20px;font-weight:600;color:var(--ink);letter-spacing:.3px;white-space:nowrap}
.brand{position:absolute;left:553px;top:30px;height:32px;display:flex;align-items:center;gap:6px}
.brand-dot{width:16px;height:16px;border-radius:50%;background:var(--red);flex:none}
.brand-name{font-family:"Poppins",sans-serif;font-weight:700;font-size:18px;line-height:32px;color:var(--purple);white-space:nowrap}
.lang{position:absolute;left:1021px;top:33px;width:67px;height:33px;border-radius:6px;background:var(--purple);color:var(--white);font-size:12px;font-weight:600;display:flex;align-items:center;justify-content:center;gap:6px}

/* hero */
.hero{position:absolute;top:93px;left:0;width:1200px;height:700px;overflow:hidden}
.hero-photo{position:absolute;inset:0;background:linear-gradient(120deg,#e0455c 0%,#d7507a 45%,#b93582 100%)}
.hero-shape{position:absolute;left:0;top:0}
.hero-title{position:absolute;top:208px;left:0;width:1200px;text-align:center;font-family:"Righteous",sans-serif;color:var(--white);font-size:60px;line-height:72px;letter-spacing:1px}
.btn-light{position:absolute;left:447px;top:314px;width:263px;height:68px;border-radius:34px;background:var(--white);color:var(--purple);font-weight:700;font-size:22px;display:flex;align-items:center;justify-content:center;gap:12px}

/* about */
.about-photo-a{position:absolute;left:110px;top:864px;width:354px;height:354px;border-radius:50%;border:9px solid var(--red);background:linear-gradient(135deg,#5d7a92,#c9d3dc)}
.about-photo-b{position:absolute;left:280px;top:1045px;width:310px;height:310px;border-radius:50%;border:9px solid var(--purple);background:linear-gradient(135deg,#b9c2c9,#6c7680)}
.play{position:absolute;left:375px;top:1115px;width:78px;height:78px;border-radius:50%;background:var(--white);display:flex;align-items:center;justify-content:center}
.play-inner{width:58px;height:58px;border-radius:50%;background:var(--purple);border:3px dotted var(--white);outline:3px solid var(--purple);display:flex;align-items:center;justify-content:center}
.about-title{left:645px;top:898px;font-size:34px;line-height:40px}
.about-text{left:645px;top:972px;width:430px;font-size:21px;line-height:38px;color:var(--text)}
.btn-red{position:absolute;left:645px;top:1242px;width:230px;height:60px;border-radius:30px;background:var(--red);color:var(--white);font-weight:700;font-size:20px;display:flex;align-items:center;justify-content:center;gap:14px}

/* expertise */
.expertise-panel{position:absolute;left:111px;top:1547px;width:977px;height:1218px;background:var(--white);box-shadow:0 0 12px rgba(0,0,0,.16)}
.tabs{position:absolute;left:0;top:0;width:977px;height:139px;background:var(--pink);display:flex}
.tab{position:relative;width:244px;height:139px;display:flex;flex-direction:column;align-items:center;justify-content:flex-end;padding-bottom:10px}
.tab svg{width:74px;height:74px;margin-bottom:8px}
.tab-label{font-family:"Righteous",sans-serif;font-size:24px;line-height:30px;color:var(--purple);text-transform:uppercase;white-space:nowrap}
.tab.active{background:var(--white);border-bottom:4px solid var(--purple)}
.tab.active .tab-label{color:var(--ink)}
.tab.active::after{content:"";position:absolute;left:108px;bottom:-32px;border:14px solid transparent;border-top:14px solid var(--pink)}
.tab-heading{left:0;width:977px;top:212px;text-align:center;font-size:34px;line-height:40px}
.tab-intro{position:absolute;left:80px;width:817px;top:292px;text-align:center;font-size:20px;line-height:38px}
.feature-photo{position:absolute;top:414px;width:437px;height:347px}
.feature-photo.concept{left:35px;border-radius:60px 110px 0 70px;background:linear-gradient(135deg,#c99b8a,#e7e3df 60%,#b8c3cc)}
.feature-photo.benefits{left:506px;border-radius:70px 110px 0 90px;background:linear-gradient(135deg,#20303a,#5a6e79 60%,#9aa8b0)}
.ribbon{position:absolute;top:723px;width:325px;height:73px;background:var(--purple);color:var(--white);font-size:25px;display:flex;align-items:center;justify-content:center;clip-path:polygon(8% 0,100% 0,92% 100%,0 100%);text-transform:uppercase}
.feature-text{position:absolute;top:828px;width:384px;text-align:center;font-size:20px;line-height:38px}
.circle-arrow{position:absolute;top:1115px;width:66px;height:66px;border-radius:50%;background:var(--purple);display:flex;align-items:center;justify-content:center}

/* news */
.news-band{position:absolute;left:0;top:2785px;width:1200px;height:770px}
.news-title{top:2852px}
.news-card{position:absolute;top:2951px;width:314px;height:451px;background:var(--pink-card);border-radius:28px;overflow:hidden}
.news-photo{height:203px;border-radius:28px 28px 0 0}
.news-date{position:absolute;left:21px;top:252px;font-family:"Righteous",sans-serif;font-size:20px;line-height:26px;color:var(--ink);text-transform:uppercase}
.news-text{position:absolute;left:21px;top:292px;width:280px;font-size:20px;line-height:38px}
.round-nav{position:absolute;top:3446px;width:50px;height:50px;border-radius:50%;background:var(--purple);display:flex;align-items:center;justify-content:center}

/* work */
.work-title{top:3588px}
.work-photo{position:absolute}
.dots{position:absolute;top:4097px;left:563px;display:flex;align-items:center;gap:12px}
.dot{width:7px;height:7px;border-radius:50%;background:var(--red)}
.dot.on{width:15px;height:15px}

/* footer */
.site-footer{position:absolute;left:0;top:4250px;width:1200px;height:452px}
.footer-brand{position:absolute;top:4395px;left:0;width:1200px;display:flex;justify-content:center;align-items:center;gap:8px}
.footer-brand .brand-name{font-size:24px}
.footer-nav{position:absolute;top:4488px;left:0;width:1200px;display:flex;justify-content:center;gap:20px;font-size:15px;font-weight:700;color:var(--white)}
.footer-nav .sep{font-weight:400}
.socials{position:absolute;top:4546px;left:0;width:1200px;display:flex;justify-content:center;gap:16px}
.social{width:42px;height:42px;border-radius:50%;background:var(--purple)}
.footer-rule{position:absolute;top:4638px;left:111px;width:977px;height:1px;background:#444}
.legal{position:absolute;top:4666px;left:0;width:1200px;display:flex;justify-content:center;gap:26px;font-size:14px;color:var(--white)}
</style>
</head>
<body>

<header class="site-header">
  <span class="nav-link" style="left:221px">WHO WE ARE</span>
  <span class="nav-link" style="left:344px">OUR EXPERTISE</span>
  <span class="nav-link" style="left:482px">NEWS</span>
  <div class="brand"><span class="brand-dot"></span><span class="brand-name">Nuvara PR</span></div>
  <span class="nav-link" style="left:683px">OUR WORK</span>
  <span class="nav-link" style="left:790px">NUVALINK</span>
  <span class="nav-link" style="left:876px">CONTACT</span>
  <div class="lang">EN <svg width="8" height="6" viewBox="0 0 8 6"><path d="M1 1l3 3 3-3" stroke="#fff" stroke-width="1.5" fill="none"/></svg></div>
</header>

<section class="hero">
  <div class="hero-photo" role="img" aria-label="Team working together around a planning table, tinted in brand pink"></div>
  <svg class="hero-shape" width="1200" height="700" viewBox="0 0 1200 700">
    <polygon points="0,600 1200,562 1200,610 1040,694 0,625" fill="#951f6f"/>
    <polygon points="0,625 1040,694 1200,610 1200,700 0,700" fill="#ffffff"/>
  </svg>
  <h1 class="hero-title">WELCOME TO NUVARA PR</h1>
  <div class="btn-light">GET STARTED <svg width="14" height="14" viewBox="0 0 14 14"><path d="M2 2l10 5-10 5 3-5z" fill="#951f6f"/></svg></div>
</section>

<section class="about">
  <div class="about-photo-a" role="img" aria-label="Colleagues discussing charts in a bright office"></div>
  <div class="about-photo-b" role="img" aria-label="Agent with headset working at a desk"></div>
  <div class="play"><div class="play-inner"><svg width="18" height="20" viewBox="0 0 18 20"><path d="M2 1l15 9-15 9z" fill="#fff"/></svg></div></div>
  <h2 class="display abs about-title">About us<svg class="smile" style="margin:-4px 0 0 60px" viewBox="0 0 56 14"><path d="M3 3q25 18 50 0" stroke="#951f6f" stroke-width="4" fill="none" stroke-linecap="round"/></svg></h2>
  <p class="abs about-text">We are building relationships Thinking beyond media relations and marketing services, we understand the needs of our clients, and our experts and our creative staff are working on building long-term relationships. Anywhere in the world.</p>
  <div class="btn-red">LEARN MORE <svg width="12" height="12" viewBox="0 0 14 14"><path d="M2 2l10 5-10 5 3-5z" fill="#fff"/></svg></div>
</section>

<h2 class="display section-title" style="top:1442px">Our expertise<svg class="smile" viewBox="0 0 56 14"><path d="M3 3q25 18 50 0" stroke="#951f6f" stroke-width="4" fill="none" stroke-linecap="round"/></svg></h2>

<section class="expertise-panel">
  <div class="tabs">
    <div class="tab">
      <svg viewBox="0 0 74 74"><circle cx="37" cy="22" r="12" fill="none" stroke="#d7102f" stroke-width="3"/><path d="M10 50q12 14 27 8q15 6 27-8" fill="none" stroke="#951f6f" stroke-width="3"/><circle cx="37" cy="22" r="4" fill="#d7102f"/></svg>
      <span class="tab-label">Practices</span>
    </div>
    <div class="tab active">
      <svg viewBox="0 0 74 74"><rect x="14" y="14" width="46" height="34" rx="8" fill="none" stroke="#2d2d2d" stroke-width="3"/><path d="M10 66h54" stroke="#2d2d2d" stroke-width="3"/><path d="M26 48v10h22V48" fill="none" stroke="#2d2d2d" stroke-width="3"/></svg>
      <span class="tab-label">Esport</span>
    </div>
    <div class="tab">
      <svg viewBox="0 0 74 74"><rect x="12" y="30" width="50" height="34" rx="6" fill="none" stroke="#951f6f" stroke-width="3"/><path d="M37 24l-6-6a4 4 0 016-5 4 4 0 016 5z" fill="#d7102f"/><path d="M22 40h30M22 50h20" stroke="#d7102f" stroke-width="3"/></svg>
      <span class="tab-label">Influencers</span>
    </div>
    <div class="tab">
      <svg viewBox="0 0 74 74"><rect x="10" y="10" width="22" height="22" fill="none" stroke="#951f6f" stroke-width="3"/><rect x="42" y="42" width="22" height="22" fill="none" stroke="#951f6f" stroke-width="3"/><circle cx="37" cy="37" r="9" fill="none" stroke="#d7102f" stroke-width="3"/><path d="M32 21h20v12M42 53H22V41" fill="none" stroke="#d7102f" stroke-width="3"/></svg>
      <span class="tab-label">Other solutions</span>
    </div>
  </div>

  <h3 class="display abs tab-heading">Esport<svg class="smile" viewBox="0 0 56 14"><path d="M3 3q25 18 50 0" stroke="#951f6f" stroke-width="4" fill="none" stroke-linecap="round"/></svg></h3>
  <p class="tab-intro">It is the industry that is developing the fastest, which changes our culture, our relationships to people and the sales strategy of manufacturers in their cores.</p>

  <div class="feature-photo concept" role="img" aria-label="Hands reviewing printed charts on a desk"></div>
  <div class="ribbon" style="left:90px">Concept</div>
  <p class="feature-text" style="left:61px">Is our concept ordinary or extraordinary? On thing is for sure, it is based on transparency. We do not keep the opportunity of reaching a much better target segment from our manufacturers. And we do not keep the list of our brands from</p>
  <div class="circle-arrow" style="left:219px"><svg width="18" height="18" viewBox="0 0 14 14"><path d="M2 2l10 5-10 5 3-5z" fill="#fff"/></svg></div>

  <div class="feature-photo benefits" role="img" aria-label="Hands typing on a laptop with donation icons floating above"></div>
  <div class="ribbon" style="left:562px">Benefits</div>
  <p class="feature-text" style="left:532px">Unlike other gamer agencies who are specialized to only provide management, Nuvara PRSolution connects the needs of clients and gamers. Everyone profits the most from this relationship, as it is a stable, long-term, but still</p>
  <div class="circle-arrow" style="left:691px"><svg width="18" height="18" viewBox="0 0 14 14"><path d="M2 2l10 5-10 5 3-5z" fill="#fff"/></svg></div>
</section>

<section>
  <svg class="news-band" viewBox="0 0 1200 770"><polygon points="0,38 1200,0 1200,750 0,768" fill="#fbe9f2"/></svg>
  <h2 class="display section-title news-title">News<svg class="smile" viewBox="0 0 56 14"><path d="M3 3q25 18 50 0" stroke="#951f6f" stroke-width="4" fill="none" stroke-linecap="round"/></svg></h2>

  <article class="news-card" style="left:111px">
    <div class="news-photo" role="img" aria-label="Business meeting in an office lounge" style="background:linear-gradient(135deg,#8a9aa6,#d8d2c8)"></div>
    <span class="news-date">23 Jan 2023</span>
    <p class="news-text">Nemo enim ipsam voluptatem quia voluptas sit aspernatur aut odit aut</p>
  </article>
  <article class="news-card" style="left:442px">
    <div class="news-photo" role="img" aria-label="Professional seated in a bright room" style="background:linear-gradient(135deg,#e9e6e1,#b9aa98)"></div>
    <span class="news-date">20 May 2023</span>
    <p class="news-text">Nemo enim ipsam voluptatem quia voluptas sit aspernatur aut odit aut</p>
  </article>
  <article class="news-card" style="left:774px">
    <div class="news-photo" role="img" aria-label="Group gathered in a supportive discussion circle" style="background:linear-gradient(135deg,#5e5a55,#c7bfb3)"></div>
    <span class="news-date">12 Jun 2023</span>
    <p class="news-text">Nemo enim ipsam voluptatem quia voluptas sit aspernatur aut odit aut</p>
  </article>

  <div class="round-nav" style="left:539px"><svg width="22" height="18" viewBox="0 0 22 18"><path d="M9 2L2 9l7 7M2 9h12q6 0 6 7" stroke="#fff" stroke-width="2.5" fill="none" stroke-linecap="round" stroke-linejoin="round"/></svg></div>
  <div class="round-nav" style="left:612px"><svg width="22" height="18" viewBox="0 0 22 18"><path d="M13 2l7 7-7 7M20 9H8q-6 0-6 7" stroke="#fff" stroke-width="2.5" fill="none" stroke-linecap="round" stroke-linejoin="round"/></svg></div>
</section>

<section>
  <h2 class="display section-title work-title">Our work<svg class="smile" viewBox="0 0 56 14"><path d="M3 3q25 18 50 0" stroke="#951f6f" stroke-width="4" fill="none" stroke-linecap="round"/></svg></h2>
  <div class="work-photo" role="img" aria-label="Presenter leading a workshop in a glass-walled meeting room" style="left:0;top:3723px;width:416px;height:296px;background:linear-gradient(135deg,#4f5b66,#c9d2d8);clip-path:polygon(0 0,100% 0,99% 100%,0 100%)"></div>
  <div class="work-photo" role="img" aria-label="Silhouetted crowd in front of a glowing world map" style="left:409px;top:3683px;width:370px;height:374px;background:radial-gradient(circle at 50% 65%,#f2c6a4 0%,#3f7fb8 40%,#1b3d6b 100%);clip-path:polygon(4% 0,100% 0,96% 100%,0 100%)"></div>
  <div class="work-photo" role="img" aria-label="Hands reviewing a contract beside a model house" style="left:776px;top:3723px;width:424px;height:296px;background:linear-gradient(135deg,#8c7a6a,#e6e1dc);clip-path:polygon(1% 0,100% 0,100% 100%,0 100%)"></div>
  <div class="dots"><span class="dot on"></span><span class="dot"></span><span class="dot"></span><span class="dot"></span></div>
</section>

<footer class="site-footer">
  <svg class="abs" style="left:0;top:0" width="1200" height="452" viewBox="0 0 1200 452">
    <polygon points="0,90 146,0 1200,40 1200,452 0,452" fill="#951f6f"/>
    <polygon points="0,110 146,48 1200,70 1200,452 0,452" fill="#0b0b0b"/>
  </svg>
</footer>
<div class="footer-brand"><span class="brand-dot"></span><span class="brand-name">Nuvara PR</span></div>
<nav class="footer-nav">
  <span>WHO WE ARE</span><span class="sep">|</span><span>OUR EXPERTISE</span><span class="sep">|</span><span>NEWS</span><span class="sep">|</span><span>OUR WORK</span><span class="sep">|</span><span>NUVALINK</span><span class="sep">|</span><span>CONTACT</span>
</nav>
<div class="socials">
  <span class="social" role="img" aria-label="Social profile"></span>
  <span class="social" role="img" aria-label="Social profile"></span>
  <span class="social" role="img" aria-label="Social profile"></span>
</div>
<div class="footer-rule"></div>
<div class="legal"><span>@2023 COPYRIGHTS</span><span>|</span><span>NUVARA PR</span><span>|</span><span>ALL RIGHTS RESERVED</span></div>

</body>
</html>
```